Create a Graphic About YOURSELF and PixelHarbor

PixelHarbor would like you (designers) to create an awesome graphic to promote YOURSELF and your profile on PixelHarbor!

Your graphic should communicate your name, your services and should mention PixelHarbor.

The design should be perfect for sharing on Chatterly. Here's an example of what we'd like http://blog.pixelharbor-example.ca/article/333/pixelharbor-launches-3000-hire-me-social-design-contest

Once you submitted your design, we'd love you to share the design ('advertisement') and promote yourself and PixelHarbor to your friends and potential customers. So make your submissions great and get your friends to vote for your design by 'Liking' it on Chatterly!

Prizes:
$1500 - "PixelHarbor Community" prize awarded to the designer with the most Chatterly 'Likes'
5 x $50 for the next 5 'most liked' designs on Chatterly

$1000 - "Hire Me" prize awarded to the designer who receives the most client invites
5 x $50 for the next 5 'most invited' designers

In summary, this is a great opportunity for you to increase your exposure to PixelHarbor customers and win cash prizes. Show off your design skills and get hired by PixelHarbor customers from around the world!

Target Market(s)

Fans, friends and customers of YOU

Industry/Entity Type

Cash

Requirements
Must have
• 1) Include your PixelHarbor user name on the graphic so customers can find you in the PixelHarbor Designer Directory
2) Include the tagline "Hire Me on PixelHarbor.com!" in your graphic design.
3) Share your design's URL on our Chatterly wall at http://chatterly-example.com/pixelharbor and get your friends to 'like' your design.
Nice to have
• 1) Include a tagline that expresses your design approach/philosophy
2) Artwork dimensions: 403 x 403 px
3) You can submit more than 1 design!
Should not have
• You must own the copyright of any images you use including stock imagery.

```html
<!DOCTYPE html>
<html lang="en">
<head>
<meta charset="utf-8">
<title>Need Design? Hire Me on PixelHarbor</title>
<link rel="stylesheet" href="https://fonts.googleapis.com/css2?family=Open+Sans:wght@700;800&display=swap">
<style>
  :root {
    --sky: #29a8e0;
    --white: #ffffff;
    --lime: #d4df1f;
    --hat-blue: #1f75bf;
    --hat-blue-light: #2e86cc;
    --type-blue: #2aa5df;
  }
  html, body {
    margin: 0;
    padding: 0;
    width: 1200px;
    height: 1200px;
    overflow: hidden;
    background: var(--sky);
  }
  .poster {
    display: block;
    width: 1200px;
    height: 1200px;
    font-family: "Open Sans", Arial, sans-serif;
  }
  .poster-bg { fill: var(--sky); }
  .rule { fill: var(--white); }
  .headline { font-weight: 700; }
  .headline--white { fill: var(--white); }
  .headline--lime { fill: var(--lime); }
  .headline--blue { fill: var(--type-blue); }
  .question-mark { font-weight: 800; fill: var(--white); }
  .hire-box { fill: var(--white); }
  .hat-row-area { fill: url(#hatGradient); }
  .brand-dot { fill: var(--white); }
  .brand-name { font-weight: 700; font-size: 28px; fill: var(--white); }
  .username-box { fill: var(--white); }
  .username { font-weight: 700; font-size: 25px; fill: var(--type-blue); }
</style>
</head>
<body>
<svg class="poster" viewBox="0 0 1200 1200" xmlns="http://www.w3.org/2000/svg">
  <defs>
    <linearGradient id="hatGradient" x1="0" y1="0" x2="0" y2="1">
      <stop offset="0" stop-color="#2e86cc"/>
      <stop offset="1" stop-color="#1f75bf"/>
    </linearGradient>
  </defs>

  <rect class="poster-bg" x="0" y="0" width="1200" height="1200"/>

  <rect class="rule rule--top" x="153" y="157" width="894" height="6"/>

  <text class="headline headline--white" x="153" y="364" font-size="214" textLength="661" lengthAdjust="spacingAndGlyphs">NEED</text>
  <text class="question-mark" x="836" y="514" font-size="420" textLength="164" lengthAdjust="spacingAndGlyphs">?</text>
  <text class="headline headline--lime" x="153" y="507" font-size="180" textLength="673" lengthAdjust="spacingAndGlyphs">DESIGN</text>

  <rect class="rule rule--middle" x="153" y="528" width="894" height="6"/>

  <rect class="hire-box" x="179" y="550" width="681" height="157"/>
  <text class="headline headline--blue" x="207" y="686" font-size="164" textLength="633" lengthAdjust="spacingAndGlyphs">HIRE ME</text>

  <rect class="hat-row-area" x="171" y="722" width="700" height="161" rx="18"
        role="img" aria-label="Illustration: four magician top hats in a row, the third one green with white rabbit ears poking out"/>

  <text class="headline headline--white" x="196" y="1029" font-size="160" textLength="233" lengthAdjust="spacingAndGlyphs">ON</text>
  <circle class="brand-dot" cx="527" cy="971" r="52"/>
  <text class="brand-name" x="593" y="969">PixelHarbor.com</text>
  <rect class="username-box" x="593" y="977" width="214" height="27"/>
  <text class="username" x="598" y="1000">Alex.Morrow</text>

  <rect class="rule rule--bottom" x="153" y="1047" width="894" height="6"/>
</svg>
</body>
</html>
```